Harmony Swift Care Business card

We want a business card that matches our business theme. Our website is www.swiftcarehub.example
The company name is Harmony Swift Care
The persons having the business cards will be doctors
My logo is attached.
We have a drive-thru medical center where our motto is Fast, Reliable, and Convenient. Our goal is to change the medical space while utilizing technologies, keeping a professional and clean look

Medical

Info on the card should be: Name, Position, Cell number, website, email address, possibly the office line as well

Requirements
Must have
• Logo
Nice to have
• Professional medical feel with our logo colors incorporated

```html
<!DOCTYPE html>
<html lang="en">
<head>
<meta charset="utf-8">
<title>Harmony Swift Care – Business Card</title>
<link href="https://fonts.googleapis.com/css2?family=Quicksand:wght@500;600;700&display=swap" rel="stylesheet">
<style>
  :root{
    --bg:#cfcfcf;
    --white:#ffffff;
    --navy:#1d3f94;
    --blue:#2a56b0;
    --sky:#4cc3ee;
    --pale:#a9d6f0;
    --ink:#333333;
  }
  html,body{margin:0;padding:0;overflow:hidden;}
  body{
    width:1200px;height:876px;background:var(--bg);
    font-family:"Quicksand",sans-serif;
    display:flex;align-items:center;justify-content:center;gap:60px;
  }
  .card{
    width:540px;height:310px;background:var(--white);position:relative;overflow:hidden;
    box-shadow:0 6px 16px rgba(0,0,0,.18);
  }
  .bars{position:absolute;left:0;right:0;}
  .brand{
    display:flex;align-items:center;gap:12px;justify-content:center;
  }
  .brand-name{
    font-weight:700;font-size:30px;color:var(--blue);line-height:1;
  }
  .brand-dot{
    width:34px;height:34px;border-radius:50%;border:5px solid var(--blue);box-sizing:border-box;
  }
  .tagline{
    font-weight:600;font-size:12px;letter-spacing:.5px;color:var(--ink);text-align:center;margin-top:10px;
  }
  .site{
    font-weight:500;font-size:11px;letter-spacing:4px;color:var(--ink);text-align:center;margin-top:8px;
  }

  /* Back card */
  .card-back .bars{top:86px;height:72px;
    background:linear-gradient(to top,var(--pale),rgba(169,214,240,0));}
  .card-back .logo-block{position:absolute;top:34px;left:0;right:0;}
  .card-back .brand-name{font-size:24px;}
  .card-back .brand-dot{width:28px;height:28px;border-width:4px;}
  .card-back .tagline{font-size:10px;margin-top:6px;}
  .info-band{
    position:absolute;left:0;right:0;bottom:0;height:146px;
    background:linear-gradient(160deg,var(--blue),var(--navy));
    border-top:6px solid var(--sky);
    display:flex;justify-content:space-between;padding:26px 28px;box-sizing:border-box;color:var(--white);
  }
  .centre-name{font-weight:700;font-size:20px;letter-spacing:.5px;line-height:1.1;}
  .centre-sub{font-weight:500;font-size:20px;line-height:1.1;}
  .centre-site{font-size:9px;letter-spacing:3px;margin-top:10px;}
  .contact-list{list-style:none;margin:0;padding:0;font-size:11px;font-weight:600;line-height:1.45;max-width:290px;}
  .contact-list li{display:flex;gap:8px;align-items:flex-start;}
  .contact-list svg{flex:none;margin-top:1px;}

  /* Front card */
  .card-front .bars{top:0;height:110px;
    background:linear-gradient(to bottom,var(--pale),rgba(76,195,238,.15) 70%,rgba(255,255,255,0));}
  .card-front .logo-block{position:absolute;top:118px;left:0;right:0;}
</style>
</head>
<body>

<section class="card card-back">
  <div class="bars" role="img" aria-label="Vertical light-blue bar pattern rising toward the contact band"></div>
  <div class="logo-block">
    <div class="brand"><span class="brand-name">Harmony Swift Care</span><span class="brand-dot"></span></div>
    <div class="tagline">FAST | RELIABLE | CONVENIENT</div>
  </div>
  <div class="info-band">
    <div class="centre">
      <div class="centre-name">HARMONY</div>
      <div class="centre-sub">Health Centre</div>
      <div class="centre-site">www.swiftcarehub.example</div>
    </div>
    <ul class="contact-list">
      <li><svg width="12" height="12" viewBox="0 0 12 12"><circle cx="6" cy="6" r="6" fill="#fff"/><path d="M4 3l1.2 1.4-.6.8a4 4 0 002.2 2.2l.8-.6L9 8l-.7.9C6 8.8 3.2 6 3.1 3.7z" fill="#1d3f94"/></svg>876-555-0142</li>
      <li><svg width="12" height="12" viewBox="0 0 12 12"><circle cx="6" cy="6" r="6" fill="#fff"/><path d="M6 2.5a2.3 2.3 0 00-2.3 2.3C3.7 6.5 6 9.5 6 9.5s2.3-3 2.3-4.7A2.3 2.3 0 006 2.5zm0 3.2a.9.9 0 110-1.8.9.9 0 010 1.8z" fill="#1d3f94"/></svg>Unit 4, Harbourview Plaza, 9 Coral Lane, Seaview, Jamaica</li>
      <li><svg width="12" height="12" viewBox="0 0 12 12"><circle cx="6" cy="6" r="6" fill="#fff"/><rect x="3" y="4" width="6" height="4.2" fill="none" stroke="#1d3f94"/><path d="M3 4l3 2.3L9 4" fill="none" stroke="#1d3f94"/></svg>info@swiftcarehub.example</li>
      <li><svg width="12" height="12" viewBox="0 0 12 12"><circle cx="6" cy="6" r="6" fill="#fff"/><circle cx="6" cy="6" r="3.3" fill="none" stroke="#1d3f94"/><path d="M6 4v2l1.3 1" fill="none" stroke="#1d3f94"/></svg>Mon–Sat 9.00AM–6.00PM</li>
    </ul>
  </div>
</section>

<section class="card card-front">
  <div class="bars" role="img" aria-label="Vertical blue bar pattern hanging from the top edge"></div>
  <div class="logo-block">
    <div class="brand"><span class="brand-name">Harmony Swift Care</span><span class="brand-dot"></span></div>
    <div class="tagline">FAST | RELIABLE | CONVENIENT</div>
    <div class="site">www.swiftcarehub.example</div>
  </div>
</section>

</body>
</html>
```